Counseling Practice Business Card

I need a professional looking business card incorporating my new logo that was just completed. Card needs to incorporate my name and title, description of my specialty, my address, my phone number, my fax number, my email and my website URL. I need to be able to choose design on/with different paper colors and textures.
I do not have a lot of business card ideas so I am open to anything but I want bold,sharp, clear card without additional designs other than my logo (see attached file info). I am open to different color backgrounds or paper colors including black. I do not like traditional brackets around area codes in phone number or dashes between numbers in phone number. Am open to other ways of presenting including periods between numbers as appropriate. I do not know enough to know what I like yet but I want card to coordinate and work together with my logo. My practice emphasizes natural mental health interventions so any use of color (with background paper color or the blue and green in my logo) that elicits nature is nice. In addition to black, any natural brown or wood looking background might be desirable also. Most of the offerings so far look very similar and boring.

Target Market(s)

Potential therapy clients and other professionals

Contact Information for Business Card

Card information:
Marcus T. Whitfield, Ph.D.
Licensed Clinical Psychologist
Integrative Health Coach
4812 Ferndale Pkwy NW
Suite 730
Duluth, GA 30096
(770) 555-0142 phone
(770) 555-0186 fax
drmarcuswhitfield@kelvora.com
pathbloomcounseling.com

Font styles to use
Serif
Sans Serif
Other font styles liked:
• anything that you think looks crisp, clear and easily readable

Requirements
Must have
• Any color used should coordinate with my logo design (see attached files).
• Card should be printed horizontally so top and bottom are longest sides of rectangle.
• Background color or paper color should complement and highlight logo. Do not like a white background. black, grey, brown or any color my logo would blend well with.
Nice to have
• I would like designer to utilize color to highlight letters/name or phone-fax-web symbols.
• Bottom edge of card could be highlighted if appropriate to an idea.
Should not have
• I would NOT want the card to have a pure white background at all.
• No clear cards.
• Cards should be oriented with long sides on bottom and top, NOT sides. DO NOT LIKE THIS THIN TALL ORIENTATION.

```html
<!DOCTYPE html>
<html lang="en">
<head>
<meta charset="utf-8">
<title>Pathbloom Counseling – Business Card</title>
<link rel="stylesheet" href="https://fonts.googleapis.com/css2?family=Montserrat:wght@500;600;700;800&display=swap">
<style>
  :root {
    --page: #ededed;
    --card-dark: #2b2b2b;
    --card-light: #f4f4f4;
    --brand-blue: #2f78b5;
    --brand-green: #1f7a45;
    --text-light: #ffffff;
    --shadow: rgba(0,0,0,0.18);
  }
  * { box-sizing: border-box; margin: 0; padding: 0; }
  html, body {
    width: 1200px; height: 1172px; overflow: hidden;
    background: var(--page);
    font-family: "Montserrat", sans-serif;
  }
  .card {
    position: absolute; left: 180px;
    width: 840px; height: 480px;
    overflow: hidden;
    box-shadow: 0 10px 28px var(--shadow);
  }
  .card--front { top: 80px; background: var(--card-dark); }
  .card--back { top: 612px; background: var(--card-dark);
    display: flex; align-items: center; justify-content: center; }
  .card__shape { position: absolute; inset: 0; }
  .wordmark {
    position: absolute;
    color: var(--brand-blue);
    font-weight: 700;
    line-height: 1.05;
    letter-spacing: 1px;
  }
  .card--front .wordmark { left: 70px; top: 150px; font-size: 46px; }
  .card--back .wordmark { position: static; font-size: 62px; text-align: center; }
  .details {
    position: absolute; left: 530px; top: 100px; width: 300px;
    color: var(--text-light);
  }
  .details__name {
    font-size: 15.5px; font-weight: 800; text-transform: uppercase;
    color: var(--brand-blue); white-space: nowrap; margin-bottom: 8px;
  }
  .details__name .degree { color: var(--brand-green); }
  .details__role { font-size: 15px; font-weight: 500; line-height: 1.45; }
  .details__address { font-size: 15px; font-weight: 500; line-height: 1.45; margin-top: 26px; }
  .contact { list-style: none; margin-top: 22px; }
  .contact__item {
    display: flex; align-items: center; gap: 10px;
    font-size: 15px; font-weight: 500; line-height: 1.6; white-space: nowrap;
  }
  .contact__icon { width: 16px; height: 16px; flex: none; color: var(--brand-blue); }
</style>
</head>
<body>
  <section class="card card--front">
    <svg class="card__shape" viewBox="0 0 840 480" aria-hidden="true">
      <path d="M0 0 H492 C 542 172 462 425 272 480 H0 Z" fill="var(--brand-blue)"/>
      <path d="M0 0 H470 C 520 170 440 420 250 480 H0 Z" fill="var(--card-light)"/>
    </svg>
    <div class="wordmark">Pathbloom<br>Counseling</div>
    <div class="details">
      <p class="details__name">Marcus T. Whitfield, <span class="degree">Ph.D.</span></p>
      <p class="details__role">Licensed clinical psychologist<br>Integrative health coach</p>
      <p class="details__address">4812 Ferndale Pkwy NW<br>Suite 730, Duluth, GA 30096</p>
      <ul class="contact">
        <li class="contact__item">
          <svg class="contact__icon" viewBox="0 0 16 16"><path d="M4 1 L6 4.5 L4.5 6 C5.5 8 8 10.5 10 11.5 L11.5 10 L15 12 L13 15 C7 14 2 9 1 3 Z" fill="currentColor"/></svg>
          (770) 555-0142
        </li>
        <li class="contact__item">
          <svg class="contact__icon" viewBox="0 0 16 16"><rect x="4" y="1" width="8" height="4" fill="currentColor"/><rect x="1" y="6" width="14" height="6" rx="1" fill="currentColor"/><rect x="4" y="10" width="8" height="5" fill="currentColor" stroke="var(--card-dark)" stroke-width="1"/></svg>
          (770) 555-0186
        </li>
        <li class="contact__item">
          <svg class="contact__icon" viewBox="0 0 16 16"><rect x="1" y="3" width="14" height="10" fill="none" stroke="currentColor" stroke-width="1.5"/><path d="M1 3 L8 9 L15 3" fill="none" stroke="currentColor" stroke-width="1.5"/></svg>
          drmarcuswhitfield@kelvora.com
        </li>
        <li class="contact__item">
          <svg class="contact__icon" viewBox="0 0 16 16" fill="none" stroke="currentColor" stroke-width="1.3"><circle cx="8" cy="8" r="6.5"/><ellipse cx="8" cy="8" rx="3" ry="6.5"/><path d="M1.5 8 H14.5 M2.5 4.8 H13.5 M2.5 11.2 H13.5"/></svg>
          www.pathbloomcounseling.com
        </li>
      </ul>
    </div>
  </section>

  <section class="card card--back">
    <div class="wordmark">Pathbloom<br>Counseling</div>
  </section>
</body>
</html>
```